Awesome Flyer for Tactical Emergency Response Services

We need a Flyer for Emergency Rapid Response services for my company ferncrest Security Services Ltd. , we are a security guisard service based in Trinidad in the Caribbean.
The flyer will include price and pictures of our tactical team. must be clear concise, and strong.

Rapid response services is where customers pay a monthly fee and if they have any security issues they call us and we immediately respond to their home or business to ensure their safety and security.

Target Market(s)

Homeowners; people worried about home security such as home invasions etc.

Requirements
Must have
• Company Logo prominent

```html
<!DOCTYPE html>
<html lang="en">
<head>
<meta charset="utf-8">
<title>ferncrest Security Services Ltd. – Rapid Response Flyer</title>
<link rel="stylesheet" href="https://fonts.googleapis.com/css2?family=Bebas+Neue&family=Open+Sans:wght@400;600;700&display=swap">
<style>
  :root {
    --brand-red: #d71f26;
    --deep-red: #b5161c;
    --ink: #111111;
    --charcoal: #1c1c1c;
    --slate: #2e2e2e;
    --paper: #f3f3f3;
    --white: #ffffff;
    --text-dark: #222222;
    --text-grey: #3a3a3a;
  }
  * { box-sizing: border-box; margin: 0; padding: 0; }
  html, body {
    width: 974px; height: 1200px; overflow: hidden;
    background: var(--paper);
    font-family: "Open Sans", Arial, sans-serif;
  }
  .flyer { position: relative; width: 974px; height: 1200px; overflow: hidden; background: var(--paper); }

  .header { position: absolute; left: 0; top: 0; width: 974px; height: 162px; background: var(--paper); }
  .brand { position: absolute; left: 46px; top: 48px; display: flex; align-items: center; gap: 16px; }
  .brand-dot { width: 58px; height: 58px; border-radius: 50%; background: var(--brand-red); }
  .brand-name {
    font-family: "Bebas Neue", Arial, sans-serif; font-size: 44px; line-height: 1;
    color: var(--brand-red); letter-spacing: 1px; max-width: 420px;
  }
  .tagline {
    position: absolute; right: 22px; top: 90px;
    font-weight: 600; font-size: 25px; color: var(--ink); letter-spacing: -0.3px;
  }

  .team-photo {
    position: absolute; left: 0; top: 160px; width: 974px; height: 470px;
    background: linear-gradient(180deg, #bdbdb8 0%, #a9a8a2 45%, #6d6b66 80%, #4a4844 100%);
  }

  .response-panel {
    position: absolute; left: 0; top: 0; width: 974px; height: 1200px; pointer-events: none;
  }

  .headline {
    position: absolute; left: 38px; top: 645px;
    font-family: "Bebas Neue", Arial, sans-serif; font-size: 46px; line-height: 1;
    color: var(--white); letter-spacing: 0.5px;
  }
  .headline .accent { color: var(--brand-red); }

  .feature {
    position: absolute; top: 728px; width: 300px; text-align: center;
    color: var(--white); font-size: 20px; line-height: 28px;
  }
  .feature svg { display: block; margin: 0 auto; }
  .feature p { margin-top: 18px; }
  .feature--equipped { left: 58px; }
  .feature--around-clock { left: 333px; }
  .feature--around-clock p { margin-top: 40px; }
  .feature--peace { left: 634px; }
  .feature--peace p { margin-top: 26px; }

  .price {
    position: absolute; left: 0; width: 974px; top: 942px; text-align: center;
    font-family: "Bebas Neue", Arial, sans-serif; font-size: 44px; color: var(--white); line-height: 1;
  }
  .offer {
    position: absolute; left: 0; width: 974px; top: 997px; text-align: center;
    font-size: 20px; color: var(--brand-red);
  }

  .contact-label {
    position: absolute; left: 44px; top: 1042px;
    font-family: "Bebas Neue", Arial, sans-serif; font-size: 26px; color: var(--white); line-height: 30px;
  }

  .contact-strip {
    position: absolute; left: 0; top: 1088px; width: 974px; height: 66px; background: var(--paper);
  }
  .contact-item {
    position: absolute; top: 0; height: 66px; display: flex; align-items: center; gap: 12px;
    font-size: 21px; color: var(--text-grey);
  }
  .contact-item--email { left: 44px; }
  .contact-item--phone { left: 352px; }
  .contact-item--web { left: 690px; }
</style>
</head>
<body>
<div class="flyer">

  <div class="team-photo" role="img" aria-label="Photo of four tactical response officers in caps, vests and dark uniforms standing ready before a grey block wall"></div>

  <header class="header">
    <div class="brand">
      <span class="brand-dot"></span>
      <span class="brand-name">ferncrest Security Services Ltd.</span>
    </div>
    <p class="tagline">“Strive to the best. Soar above the rest.”</p>
  </header>

  <svg class="response-panel" width="974" height="1200" viewBox="0 0 974 1200" aria-hidden="true">
    <defs>
      <radialGradient id="panelShade" cx="50%" cy="45%" r="70%">
        <stop offset="0%" stop-color="#3a3a3a"/>
        <stop offset="60%" stop-color="#1e1e1e"/>
        <stop offset="100%" stop-color="#0c0c0c"/>
      </radialGradient>
      <linearGradient id="tabRed" x1="0" x2="1">
        <stop offset="0%" stop-color="#b5161c"/>
        <stop offset="100%" stop-color="#e5262d"/>
      </linearGradient>
    </defs>

    <!-- header divider -->
    <polygon points="470,166 560,152 974,152 974,160 563,160 474,174" fill="#d71f26"/>

    <!-- dark response panel -->
    <polygon points="0,630 614,630 664,590 974,590 974,1200 0,1200" fill="url(#panelShade)"/>
    <polygon points="600,630 652,588 974,588 974,596 658,596 606,638" fill="#d71f26"/>
    <polygon points="0,620 640,620 628,630 0,630" fill="#d71f26" opacity="0"/>

    <!-- contact tab and rule -->
    <polygon points="0,1040 334,1040 320,1072 0,1072" fill="url(#tabRed)"/>
    <rect x="350" y="1063" width="624" height="4" fill="#d71f26"/>

    <!-- footer band -->
    <rect x="0" y="1154" width="974" height="46" fill="#101010"/>
    <polygon points="0,1157 610,1157 584,1182 0,1182" fill="url(#tabRed)"/>
  </svg>

  <h1 class="headline"><span class="accent">24HR Emergency</span> Rapid Response</h1>

  <div class="feature feature--equipped">
    <svg width="78" height="92" viewBox="0 0 78 92">
      <path d="M4 4 H74 V60 L39 88 L4 60 Z" fill="#1a1a1a" stroke="#d71f26" stroke-width="2.5"/>
      <circle cx="39" cy="38" r="10" fill="#fff"/>
      <path d="M27 30 Q39 18 51 30 Z" fill="#d71f26"/>
      <rect x="26" y="29" width="26" height="4" fill="#d71f26"/>
      <path d="M22 66 Q22 52 39 51 Q56 52 56 66 Z" fill="#fff"/>
    </svg>
    <p>Fully equipped and specially trained in tactical rapid response protocols</p>
  </div>

  <div class="feature feature--around-clock">
    <svg width="78" height="92" viewBox="0 0 78 92">
      <path d="M4 4 H74 V60 L39 88 L4 60 Z" fill="#1a1a1a" stroke="#d71f26" stroke-width="2.5"/>
      <text x="39" y="42" text-anchor="middle" font-family="Bebas Neue, Arial, sans-serif" font-size="27" fill="#fff">24/7</text>
    </svg>
    <p>Protecting you 24/7</p>
  </div>

  <div class="feature feature--peace">
    <svg width="78" height="92" viewBox="0 0 78 92">
      <path d="M4 4 H74 V60 L39 88 L4 60 Z" fill="#1a1a1a" stroke="#d71f26" stroke-width="2.5"/>
      <path d="M24 40 L35 51 L56 29" fill="none" stroke="#fff" stroke-width="6" stroke-linecap="round" stroke-linejoin="round"/>
    </svg>
    <p>Delivering Peace of mind to our clients</p>
  </div>

  <p class="price">$200 + VAT per month</p>
  <p class="offer">Sign up for 12 months and receive a 10% discount</p>

  <p class="contact-label">Contact us:</p>

  <div class="contact-strip">
    <div class="contact-item contact-item--email">
      <svg width="18" height="18" viewBox="0 0 18 18" aria-hidden="true"><rect x="0" y="0" width="18" height="18" rx="3" fill="#222"/><path d="M3 5 H15 V13 H3 Z M3 5 L9 10 L15 5" fill="none" stroke="#fff" stroke-width="1.4"/></svg>
      <span>info@ferncrest-tt.com</span>
    </div>
    <div class="contact-item contact-item--phone">
      <svg width="20" height="20" viewBox="0 0 20 20" aria-hidden="true"><rect width="20" height="20" rx="3" fill="#222"/><path d="M6 4 L8 4 L9 7 L7.5 8.3 Q9 11.5 11.7 12.5 L13 11 L16 12 L16 14 Q15 16 12.5 15.5 Q6 13.5 4.5 7 Q4.3 4.8 6 4 Z" fill="#fff"/></svg>
      <span>555-0142 / 555-0187</span>
    </div>
    <div class="contact-item contact-item--web">
      <svg width="20" height="20" viewBox="0 0 20 20" aria-hidden="true"><circle cx="10" cy="10" r="10" fill="#222"/><g fill="none" stroke="#fff" stroke-width="1.2"><circle cx="10" cy="10" r="6"/><ellipse cx="10" cy="10" rx="2.6" ry="6"/><path d="M4 10 H16"/></g></svg>
      <span>www.ferncrest-tt.com</span>
    </div>
  </div>

</div>
</body>
</html>
```